Moving comapny Postcard mailer Design

I am looking for a 6x9 postcard with real images of our team. I would like to add the same review we currently have , I want the colors of the postcard to be orange and white. I want the team picture to be enlarged with the other pictures to be mimized. I will add example postcards to give rough ideas. My company is called Harlow Moving and the postcards with that name are our current postcards. The additional postcards are from other companies who have better postcards than mine. My goal is for my postcard to be better that theirs.

Target Market(s)

Wealthy people in the 35+ age group

Industry/Entity Type

Moving company

Requirements
Must have
• Beauty

```html
<!DOCTYPE html>
<html lang="en">
<head>
<meta charset="utf-8">
<title>Harlow Moving Postcard</title>
<link href="https://fonts.googleapis.com/css2?family=Oswald:wght@500;700&family=Open+Sans:wght@400;600;700&display=swap" rel="stylesheet">
<style>
  :root {
    --orange: #f26a1b;
    --orange-deep: #e0560c;
    --navy: #1d2f5c;
    --blue: #2457a6;
    --white: #ffffff;
    --bg: #e4e6e8;
    --ink: #2a2a2a;
    --star: #ffc531;
  }
  * { box-sizing: border-box; margin: 0; padding: 0; }
  html, body { width: 729px; height: 1200px; overflow: hidden; background: var(--bg); }
  body { position: relative; font-family: "Open Sans", Arial, sans-serif; }

  .postcard {
    position: absolute; left: 44px; width: 640px; height: 427px;
    background: var(--white); overflow: hidden;
    box-shadow: 0 4px 14px rgba(0,0,0,.18);
  }
  .postcard--front { top: 115px; }
  .postcard--back { top: 657px; }
  .abs { position: absolute; }
  .heading { font-family: "Oswald", Impact, sans-serif; font-weight: 700; text-transform: uppercase; line-height: 1; }

  /* front */
  .team-photo { left: 0; top: 70px; width: 640px; height: 218px;
    background: linear-gradient(180deg, #e3ebf1 0%, #b9cba6 22%, #f1f2f1 40%, #c9ccce 52%, #4a5058 66%, #5e636a 80%, #a5a7a2 100%); }
  .name-banner { left: 130px; top: 14px; width: 380px; height: 52px; background: var(--orange);
    display: flex; align-items: center; justify-content: center; color: var(--white);
    font-size: 36px; letter-spacing: 1px; }
  .ribbon-end { top: 22px; width: 34px; height: 40px; background: var(--orange-deep); }
  .ribbon-end--left { left: 104px; clip-path: polygon(0 0, 100% 0, 100% 100%, 0 100%, 30% 50%); }
  .ribbon-end--right { left: 502px; clip-path: polygon(0 0, 100% 0, 70% 50%, 100% 100%, 0 100%); }
  .review-badge { left: 18px; top: 84px; width: 184px; height: 184px; border-radius: 50%;
    background: var(--blue); border: 4px solid var(--white); color: var(--white);
    display: flex; flex-direction: column; align-items: center; justify-content: center; padding: 20px 24px; text-align: center; }
  .review-badge .stars { color: var(--star); font-size: 14px; letter-spacing: 2px; margin-bottom: 6px; }
  .review-badge p { font-size: 9px; line-height: 1.4; font-style: italic; }
  .review-badge .author { font-weight: 700; font-style: normal; margin-top: 5px; }
  .offer-band { left: 0; top: 288px; width: 640px; height: 58px; background: var(--orange); }
  .offer-stripe { left: 0; top: 346px; width: 640px; height: 6px; background: var(--navy); }
  .coupons { display: flex; gap: 10px; }
  .coupon { width: 94px; height: 48px; background: var(--white); border: 2px solid var(--white); text-align: center; overflow: hidden; }
  .coupon .amount { display: block; background: var(--orange-deep); color: var(--white); font-size: 20px; padding: 3px 0; }
  .coupon .terms { display: block; font-size: 7.5px; font-weight: 700; color: var(--navy); padding-top: 4px; white-space: nowrap; }
  .postcard--front .coupons { left: 168px; top: 293px; }
  .helper-photo { left: 18px; top: 292px; width: 135px; height: 122px; border: 4px solid var(--white);
    background: linear-gradient(160deg, #dfe4e6 0%, #9fb0bf 45%, #34456b 100%); }
  .mascot { left: 512px; top: 292px; width: 108px; height: 124px;
    background: radial-gradient(ellipse at 50% 35%, #f5a152 0%, #f0d5b4 45%, rgba(255,255,255,0) 72%); }
  .quote-cta { color: var(--navy); font-size: 25px; }
  .postcard--front .quote-cta { left: 168px; top: 362px; }
  .phone { display: flex; align-items: center; gap: 6px; font-family: "Oswald", sans-serif; font-weight: 700; color: var(--navy); font-size: 24px; }
  .phone svg { width: 22px; height: 22px; }
  .postcard--front .phone { left: 168px; top: 390px; }

  /* back */
  .headline { left: 22px; top: 22px; font-size: 48px; color: var(--navy); }
  .headline .accent { color: var(--orange); }
  .brand-mark { left: 196px; top: 30px; display: flex; align-items: center; gap: 5px;
    font-family: "Oswald", sans-serif; font-weight: 700; font-size: 11px; color: var(--orange); text-transform: uppercase; }
  .brand-mark .sq { width: 11px; height: 11px; background: var(--orange); display: block; }
  .intro { left: 22px; top: 132px; width: 292px; font-size: 9.5px; line-height: 1.45; color: var(--ink); }
  .postcard--back .coupons { left: 22px; top: 204px; }
  .postcard--back .coupon { border-color: var(--orange-deep); }
  .crew-photo { left: 22px; top: 262px; width: 292px; height: 72px;
    background: linear-gradient(90deg, #e9e4da 0%, #b8aa93 40%, #6c7077 75%, #d8dde0 100%); }
  .postcard--back .quote-cta { left: 22px; top: 348px; width: 150px; font-size: 22px; line-height: 1.1; }
  .contact { left: 186px; top: 352px; }
  .contact .phone { font-size: 21px; }
  .web { display: flex; align-items: center; gap: 6px; margin-top: 8px; font-size: 12px; font-weight: 600; color: var(--navy); }
  .web .dot { width: 14px; height: 14px; border-radius: 50%; background: var(--orange); }
  .furniture-photo { left: 330px; top: 0; width: 310px; height: 282px;
    background: linear-gradient(170deg, #cfe0ea 0%, #e6e1d6 35%, #7fb3b5 60%, #8a7f70 100%); }
  .swoosh { left: 0; bottom: 0; width: 640px; height: 40px; }
</style>
</head>
<body>

<section class="postcard postcard--front">
  <div class="abs team-photo" role="img" aria-label="Moving crew in uniforms standing in front of two white moving trucks"></div>
  <div class="abs ribbon-end ribbon-end--left"></div>
  <div class="abs ribbon-end ribbon-end--right"></div>
  <div class="abs name-banner heading">Harlow Moving</div>
  <div class="abs review-badge">
    <div class="stars">★★★★★</div>
    <p>“Harlow Moving made our move effortless. The crew was careful, fast and friendly, and every piece arrived safe. We would not trust anyone else.”</p>
    <p class="author">— Linda R.</p>
  </div>
  <div class="abs offer-band"></div>
  <div class="abs offer-stripe"></div>
  <div class="abs helper-photo" role="img" aria-label="Mover wheeling boxes on a hand truck"></div>
  <div class="abs coupons">
    <div class="coupon"><span class="amount heading">$25 Off</span><span class="terms">ON LOCAL MOVES</span></div>
    <div class="coupon"><span class="amount heading">$50 Off</span><span class="terms">ON MOVES OVER 4 HRS</span></div>
    <div class="coupon"><span class="amount heading">$100 Off</span><span class="terms">ON LONG DISTANCE</span></div>
  </div>
  <div class="abs mascot" role="img" aria-label="Cartoon moving box mascot character"></div>
  <div class="abs quote-cta heading">Get a free moving quote</div>
  <div class="abs phone">
    <svg viewBox="0 0 24 24"><path fill="#f26a1b" d="M6.6 10.8a15.1 15.1 0 0 0 6.6 6.6l2.2-2.2c.3-.3.7-.4 1-.2 1.1.4 2.3.6 3.6.6.6 0 1 .4 1 1V20c0 .6-.4 1-1 1A17 17 0 0 1 3 4c0-.6.4-1 1-1h3.5c.6 0 1 .4 1 1 0 1.3.2 2.5.6 3.6.1.3 0 .7-.2 1z"/></svg>
    555-014-2290
  </div>
</section>

<section class="postcard postcard--back">
  <div class="abs furniture-photo" role="img" aria-label="Mover carrying plastic-wrapped furniture out of a house"></div>
  <div class="abs headline heading"><span class="accent">Moving.</span><br>Made. Simple.</div>
  <div class="abs brand-mark"><span class="sq"></span>Harlow Moving</div>
  <p class="abs intro">For over ten years our crew has delivered smooth, stress-free moves across the region. We treat every home with care, arrive on time, and keep your belongings safe from start to finish.</p>
  <div class="abs coupons">
    <div class="coupon"><span class="amount heading">$25 Off</span><span class="terms">ON LOCAL MOVES</span></div>
    <div class="coupon"><span class="amount heading">$50 Off</span><span class="terms">ON MOVES OVER 4 HRS</span></div>
    <div class="coupon"><span class="amount heading">$100 Off</span><span class="terms">ON LONG DISTANCE</span></div>
  </div>
  <div class="abs crew-photo" role="img" aria-label="Movers loading boxes into a truck"></div>
  <div class="abs quote-cta heading">Get a free moving quote</div>
  <div class="abs contact">
    <div class="phone">
      <svg viewBox="0 0 24 24"><path fill="#f26a1b" d="M6.6 10.8a15.1 15.1 0 0 0 6.6 6.6l2.2-2.2c.3-.3.7-.4 1-.2 1.1.4 2.3.6 3.6.6.6 0 1 .4 1 1V20c0 .6-.4 1-1 1A17 17 0 0 1 3 4c0-.6.4-1 1-1h3.5c.6 0 1 .4 1 1 0 1.3.2 2.5.6 3.6.1.3 0 .7-.2 1z"/></svg>
      555-014-2290
    </div>
    <div class="web"><span class="dot"></span>harlowmove.com</div>
  </div>
  <svg class="abs swoosh" viewBox="0 0 640 40" preserveAspectRatio="none">
    <path d="M330 40 C 450 10, 560 8, 640 14 L640 40 Z" fill="#1d2f5c"/>
    <path d="M330 40 C 450 20, 560 20, 640 26 L640 40 Z" fill="#f26a1b"/>
  </svg>
</section>

</body>
</html>
```